Corvane Global Stationery & Logo Design

We are looking for a logo and stationary design for our business, which should include:
1) Letterhead
2) Business cards
3) A4 folders for company marketing materials
4) Envelops and
5) A4 file covers
We are international business consultants and tax advisers. We help companies with entering new markets by developing a market entry strategy, finding business partners and providing cross borders tax and finance advice.
We operate in the United Kingdom, Poland and India. Our target market includes middle and large companies from these three countries.
Company Name: Corvane Global Ltd.
Address: 12 Harrowgate Row, Pellingham, London, EC4M 3TQ,
email: hello@corvane-mail.example
Website: www.corvane-web.example
Phone: +44 (0) 20 3918 4406
Company Slogan: Clear Answers for a Crowded Age
Vision: To be the first choice for clients by delivering exceptional service through innovation and excellence
Mission: To persevere and achieve excellence in our endeavours through simplicity, respect and creativity
Values: Delivering Innovation with Creativity, Integrity, Achieving Excellence, Fun and Respect and Giving Back to Society.
Project Specification
Our preferred colour is royal blue however, we are open to ideas. We would like a design that is elegant but innovative, sleek and modern. The message we would like to convey is that we are professional and trustworthy business partners.
Please do not use Times New Roman or similar fonts.
Logo
The name of the company is Corvane Global Ltd and the logo can only include the company name although we would prefer to use only ‘Corvane Global’ without ‘Ltd’. Corvane does not need to be in capital letters.
Business Cards
Double sided business cards for our British, Polish and Indian office. The addresses should be as follows:
Corvane Global Ltd
12 Harrowgate Row, Pellingham, London, EC4M 3TQ, email: name@corvane-mail.example, www.corvane-web.example, +44 (0) 20 3918 4406
Corvane Global (Poland) sp. z o.o.
ul. Brzozowiecka 27 lok. 304, 00-812 Warszawa, name@corvane-mail.example, www.corvane-web.example
+48 (0) 22 417 5390
Corvane Global (India) Pvt. Ltd.
Trade Court, 64 Rajani Mohan Lane, 3rd Floor, Kolkata, 700 021, name@corvane-mail.example, www.corvane-web.example
+91 (0) 33 2781 6034
The names and email addresses will be confirmed once a winning design has been selected.
The business cards should include the company slogan and QR code.
Letterhead
All three addresses need to be on the letterhead. Email address should be hello@corvane-mail.example. Design of continuation sheets should be different to the front page.
A4 folders
We would like the outer and inside pages to have a slightly different design. The company slogan, vision, mission and the three offices’ addresses should also come somewhere on the folder. We do not want the design to include too many photos and would be happy with a design which does not have them at all but any other graphics are fine.
A4 file covers
We would need a front, back and side page. Company slogan and the three offices’ addresses should be included.
Envelopes
Window and regular DL and A4 envelopes.
Reason: The proposals we have received so far are not in line with our expectations so we would like to give the designer a bit more time to prepare a few new looks. Also, what we have received so far are only logos and the remaining items in our brief have not been prepared yet.

```html
<!DOCTYPE html>
<html lang="en">
<head>
<meta charset="utf-8">
<title>Corvane Global Stationery</title>
<link rel="stylesheet" href="https://fonts.googleapis.com/css2?family=Barlow:wght@500&family=Noto+Serif:wght@400&display=swap">
<style>
  :root {
    --backdrop: #2d2440;
    --paper: #ececed;
    --paper-edge: #e2e2e4;
    --paper-plain: #f3f3f4;
    --ink: #3b3b3d;
    --ink-soft: #8a8a8e;
    --brand: #4b3b8f;
  }
  * { margin: 0; padding: 0; box-sizing: border-box; }
  html, body { width: 1200px; height: 832px; overflow: hidden; }
  body { background: var(--backdrop); position: relative; font-family: "Noto Serif", serif; color: var(--ink); }

  .sheet { position: absolute; background: linear-gradient(160deg, var(--paper) 0%, var(--paper-edge) 100%); }
  .sheet--continuation { left: 192px; top: 192px; width: 345px; height: 483px; background: var(--paper-plain); }
  .sheet--letterhead { left: 251px; top: 253px; width: 343px; height: 486px; }
  .folder { position: absolute; left: 658px; top: 92px; width: 373px; height: 495px; border-radius: 0 6px 6px 0;
            background: linear-gradient(160deg, var(--paper) 0%, var(--paper-edge) 100%); }

  .brand { display: flex; align-items: center; gap: 6px; font-family: "Barlow", sans-serif; font-weight: 500; color: var(--ink); white-space: nowrap; }
  .brand__mark { background: var(--brand); flex: none; }

  .sheet--continuation .brand { position: absolute; left: 30px; top: 24px; font-size: 8px; }
  .sheet--continuation .brand__mark { width: 10px; height: 10px; }

  .sheet--letterhead .brand { position: absolute; left: 15px; top: 66px; font-size: 11px; }
  .sheet--letterhead .brand__mark { width: 13px; height: 13px; }

  .slogan { position: absolute; left: 121px; top: 38px; width: 200px; font-size: 15px; line-height: 17px; color: var(--ink); }

  .meta { position: absolute; right: 250px; top: 118px; width: 90px; text-align: right; font-size: 4.6px; line-height: 7px; color: var(--ink-soft); }
  .meta dt { color: var(--ink); font-size: 5px; margin-top: 6px; }
  .meta dt:first-child { margin-top: 0; }

  .letter-body { position: absolute; left: 121px; top: 118px; width: 190px; font-size: 4.6px; line-height: 8px; color: var(--ink-soft); }
  .letter-body p { margin-bottom: 10px; }
  .signature { margin-top: 4px; }
  .signature strong { display: block; font-weight: 400; font-size: 6px; color: var(--ink); }
  .signature span { font-size: 4.2px; letter-spacing: .3px; }

  .folder .brand { position: absolute; left: 0; right: 0; top: 232px; justify-content: center; gap: 10px; font-size: 34px; }
  .folder .brand__mark { width: 30px; height: 30px; }

  .folder-contact { position: absolute; left: 31px; top: 437px; font-size: 4.6px; line-height: 6.6px; color: var(--ink); font-style: normal; }
</style>
</head>
<body>

  <section class="sheet sheet--continuation" aria-label="Letterhead continuation sheet">
    <div class="brand"><span class="brand__mark"></span>Corvane Global</div>
  </section>

  <section class="sheet sheet--letterhead" aria-label="Letterhead front page">
    <div class="brand"><span class="brand__mark"></span>Corvane Global</div>
    <h1 class="slogan" style="font-weight:400">Clear Answers for a Crowded Age</h1>

    <dl class="meta">
      <dt>Date</dt>
      <dd>01. 11. 2015</dd>
      <dt>Address</dt>
      <dd>12 Harrowgate Row, Pellingham,<br>London, EC4M 3TQ<br>Unit Name, Location Town</dd>
    </dl>

    <div class="letter-body">
      <p>Corvane Global Ltd. welcomes partners from all regions.</p>
      <p>We are international business consultants and tax advisers. We help companies with entering new markets by developing a market entry strategy, finding business partners and providing cross borders tax and finance advice.<br>
      We operate in the United Kingdom, Poland and India. Our target market includes middle and large companies from these three countries.</p>
      <p>Vision: To be the first choice for clients by delivering exceptional service through innovation and excellence.</p>
      <p>Mission: To persevere and achieve excellence in our endeavours through simplicity, respect and creativity.</p>
      <p>Values: Delivering Innovation with Creativity, Integrity, Achieving Excellence, Fun and Respect and Giving Back to Society.</p>
      <div class="signature"><strong>Alex Marlow</strong><span>CORPORATE</span></div>
    </div>
  </section>

  <section class="folder" aria-label="A4 folder cover">
    <div class="brand"><span class="brand__mark"></span>Corvane Global</div>
    <address class="folder-contact">
      Corvane Global Ltd.<br>
      12 Harrowgate Row, Pellingham, London, EC4M 3TQ<br>
      hello@corvane-mail.example<br>
      www.corvane-web.example<br>
      +44 (0) 20 3918 4406
    </address>
  </section>

</body>
</html>
```